Brook Forge - Crypto Currency Miner Powered by Renewable Energy Website

We Need Web Pages Design for Website for Crypto Currency Miner

Serivices include:
Mining Rig Sales
Housing for Rigs turnkey on renewable energy grid
Cloud Mining term packages
Updates

http://www.vaultrigdigest.example (Competitors sites)

Target Market(s)

Investers for Mining Rigs and terms for 1,2 or 3 years of Hash rate

Industry/Entity Type

Mining

Number of Pages Required

5+ page

Font styles to use
Sans Serif

Colors
add136
9bcb3c
606060
474747
ffc214
cadf82
fbee3e
876aae
6b449b

Requirements
Must have
• Pictures of Solar, Wind and power Factor Correction units
Nice to have
• e-commerce platform so contract terms can be purchased through website
Should not have
• Heavy construction equipment

```html
<!DOCTYPE html>
<html lang="en">
<head>
<meta charset="utf-8">
<title>Brook Forge — Renewable Crypto Mining</title>
<link href="https://fonts.googleapis.com/css2?family=Open+Sans:wght@400;600;700;800&display=swap" rel="stylesheet">
<style>
:root{
  --green:#34a853;
  --green-dark:#23893f;
  --lime:#9bcb3c;
  --ink:#474747;
  --text:#606060;
  --muted:#8a8a8a;
  --grey-band:#e9e7e5;
  --dark:#1f2224;
  --darker:#151718;
  --white:#ffffff;
  --line:#dcdcdc;
}
*{box-sizing:border-box;margin:0;padding:0}
html,body{width:1200px;height:5260px;overflow:hidden}
body{font-family:"Open Sans",Arial,sans-serif;color:var(--text);background:var(--white);font-size:13px;line-height:1.6}
section,header,footer{position:relative;width:1200px;overflow:hidden}
.center{text-align:center}
.btn{display:inline-block;background:var(--green);color:var(--white);font-size:11px;font-weight:700;letter-spacing:.5px;text-transform:uppercase;padding:8px 26px;border-radius:20px}
.btn-outline{background:transparent;border:2px solid var(--white)}
.section-title{display:flex;align-items:center;justify-content:center;gap:12px;font-size:34px;font-weight:400;color:var(--ink)}
.section-title em{font-style:normal;color:var(--green)}
.title-dot{width:34px;height:34px;border-radius:50%;background:var(--green)}
.title-rule{width:70px;height:2px;background:var(--green);margin:14px auto 0}
.intro{width:720px;margin:22px auto 0;text-align:center;font-size:13px;color:var(--text)}
.ph{display:block}

/* top bar */
.topbar{height:28px;background:var(--darker);color:#9a9a9a;font-size:11px;display:flex;justify-content:space-between;align-items:center;padding:0 80px}
.topbar span{margin-right:18px}
/* header */
.site-header{height:112px;display:flex;align-items:center;justify-content:space-between;padding:0 88px;border-bottom:1px solid #eee}
.brand{display:flex;align-items:center;gap:10px;font-size:24px;font-weight:700;color:var(--green)}
.brand-dot{width:30px;height:30px;border-radius:50%;background:var(--green)}
.main-nav{display:flex;align-items:center;gap:26px;font-size:15px;font-weight:600;color:var(--ink)}
.main-nav .active{color:var(--green);border-bottom:2px solid var(--green);padding-bottom:4px}
.nav-tools{display:flex;align-items:center;gap:18px;margin-left:34px;font-size:13px}
.nav-tools .btn{border-radius:2px;padding:8px 16px}
/* hero */
.hero{height:560px;background:linear-gradient(160deg,#6f93c4 0%,#3e5f94 40%,#1d3566 70%,#0e1f42 100%)}
.hero-photo{position:absolute;inset:0}
.hero-copy{position:absolute;top:150px;width:100%;text-align:center}
.hero-kicker{font-size:44px;color:var(--white);font-weight:400}
.hero-title{font-size:78px;line-height:1.05;font-weight:700;color:var(--lime);margin-top:4px}
.hero-dots{position:absolute;bottom:26px;width:100%;display:flex;justify-content:center;gap:10px}
.hero-dots i{width:10px;height:10px;border-radius:50%;background:rgba(255,255,255,.5)}
.hero-dots i.on{background:var(--white)}
/* about */
.about{height:540px;padding:100px 0 0 120px;display:flex;gap:60px}
.about-photo{width:440px;height:310px;background:linear-gradient(180deg,#9aa2a8 0%,#6f6a60 55%,#4a4338 100%)}
.about-copy{width:460px;padding-top:4px}
.about-copy .section-title{justify-content:flex-start;font-size:30px}
.about-copy .title-dot{width:30px;height:30px}
.about-lead{font-weight:600;color:var(--ink);margin-top:14px;font-size:13px}
.about-copy p{margin-top:14px;font-size:12.5px}
.about-copy .btn{margin-top:26px}
/* services */
.services{height:728px;background:var(--grey-band);padding-top:80px}
.service-list{display:flex;justify-content:center;gap:110px;margin-top:50px}
.service{width:220px;text-align:center}
.service-icon{width:120px;height:120px;border-radius:50%;background:var(--green);border:6px solid #cfe8d5;margin:0 auto;display:flex;align-items:center;justify-content:center}
.service h3{font-size:16px;font-weight:600;color:var(--ink);margin-top:24px;line-height:1.3}
.service p{font-size:12px;margin-top:16px}
.services .btn{margin-top:46px}
/* cta band */
.cta-band{height:192px;background:var(--green);color:var(--white);text-align:center;padding-top:40px}
.cta-band small{font-size:12px;font-weight:600;letter-spacing:1px}
.cta-band h2{font-size:32px;font-weight:700;margin:8px 0 18px}
/* experts */
.experts{height:880px;padding-top:80px}
.expert-list{display:flex;justify-content:center;gap:72px;margin-top:66px}
.expert{width:288px;text-align:center}
.expert-photo{width:288px;height:388px;background:linear-gradient(180deg,#eceef0 0%,#c9ced4 60%,#2d3a4d 100%)}
.expert h4{font-size:15px;font-weight:600;color:var(--ink);margin-top:16px}
.expert span{font-size:11px;color:var(--green);font-weight:600;text-transform:uppercase}
.slider-dots{display:flex;justify-content:center;gap:10px;margin-top:40px}
.slider-dots i{width:10px;height:10px;border-radius:50%;background:#ccc}
.slider-dots i.on{background:var(--green)}
/* question */
.question{height:592px;background:radial-gradient(circle at 30% 30%,#34383a 0%,var(--dark) 55%,var(--darker) 100%);padding-top:72px;color:var(--white)}
.question .section-title{color:var(--white)}
.q-form{display:flex;justify-content:center;gap:56px;margin-top:44px}
.q-col{width:392px}
.field label{display:block;font-size:12px;font-weight:600;text-transform:uppercase;margin-bottom:6px}
.field .input{height:34px;background:var(--white);margin-bottom:26px}
.field .textarea{height:96px;background:var(--white)}
.question .btn{background:var(--white);color:var(--ink);margin-top:30px}
/* news */
.news{height:628px;padding-top:70px}
.news-list{display:flex;justify-content:center;gap:32px;margin-top:44px}
.news-card{width:300px;border:1px solid var(--line);background:var(--white)}
.news-photo{height:200px;background:linear-gradient(180deg,#dfe4e8 0%,#b9c2ca 60%,#6c7680 100%)}
.news-body{padding:18px}
.news-body h4{font-size:16px;font-weight:700;color:var(--ink);line-height:1.3}
.news-body time{display:block;font-size:11px;color:var(--green);margin-top:10px}
.news-body p{font-size:12px;margin-top:6px}
.news-body a{display:block;font-size:11px;color:var(--green);margin-top:10px;text-decoration:none}
/* newsletter */
.newsletter{height:140px;background:var(--green);display:flex;align-items:center;padding:0 140px;justify-content:space-between;color:var(--white)}
.newsletter h2{font-size:30px;font-weight:400}
.newsletter h2 strong{font-weight:800}
.sub-form{display:flex}
.sub-input{width:290px;height:40px;background:var(--white);color:var(--muted);font-size:12px;padding:11px 14px}
.sub-btn{width:160px;height:40px;border:2px solid var(--white);color:var(--white);font-size:12px;font-weight:600;text-align:center;line-height:36px}
/* feedback */
.feedback{height:420px;padding-top:60px}
.testimonial{display:flex;justify-content:center;gap:50px;align-items:center;margin-top:50px}
.person{width:140px;text-align:center}
.avatar{width:84px;height:84px;border-radius:50%;background:linear-gradient(180deg,#d7c3b8,#8e6f60);margin:0 auto}
.person h5{font-size:13px;color:var(--ink);font-weight:600;margin-top:8px}
.person span{font-size:10px;color:var(--green);text-transform:uppercase}
.quote{width:600px;font-size:13px}
.arrow{position:absolute;top:240px}
.arrow.left{left:140px}.arrow.right{right:140px}
/* footer */
.site-footer{height:400px;background:var(--dark);color:#b5b5b5;display:flex;gap:48px;padding:56px 80px 0}
.foot-col h6{font-size:15px;color:var(--white);font-weight:700;text-transform:uppercase;margin-bottom:20px}
.foot-col h6 em{font-style:normal;color:var(--green)}
.foot-about{width:250px;font-size:12px}
.foot-about .brand{font-size:22px;margin-bottom:18px}
.foot-about p{margin-bottom:14px}
.foot-list{width:240px;list-style:none;font-size:12px}
.foot-list li{margin-bottom:10px;padding-left:14px;position:relative}
.foot-list li::before{content:"";position:absolute;left:0;top:7px;width:5px;height:5px;border-radius:50%;background:var(--green)}
.posts{width:250px}
.post{display:flex;gap:12px;margin-bottom:14px;font-size:11px}
.post-thumb{width:60px;height:44px;background:linear-gradient(135deg,#6b5a3b,#c69a52)}
.post b{display:block;color:var(--white);font-size:12px}
.social{display:flex;gap:10px;margin-bottom:30px}
.social i{width:28px;height:28px;border-radius:50%;background:#3a3e40}
.call b{display:block;color:var(--white);font-size:26px;font-weight:700}
.bottom-bar{height:40px;background:var(--darker);color:#888;font-size:11px;text-align:center;line-height:40px}
</style>
</head>
<body>

<div class="topbar">
  <div><span>English</span><span>FAQ</span><span>Support</span></div>
  <div><span>Account</span><span>Register</span><span>Wishlist</span></div>
</div>

<header class="site-header">
  <div class="brand"><span class="brand-dot"></span>Brook Forge</div>
  <nav class="main-nav">
    <span class="active">Home</span><span>About</span><span>Team</span><span>Services</span><span>Products</span><span>Clients</span><span>Contact</span>
    <div class="nav-tools">
      <svg width="14" height="14" viewBox="0 0 14 14"><circle cx="6" cy="6" r="4.5" fill="none" stroke="#474747" stroke-width="2"/><line x1="9.5" y1="9.5" x2="13" y2="13" stroke="#474747" stroke-width="2"/></svg>
      <span>EN</span>
      <span class="btn">Get a Quote</span>
    </div>
  </nav>
</header>

<section class="hero">
  <div class="hero-photo" role="img" aria-label="Rows of solar panels under a blue sky"></div>
  <div class="hero-copy">
    <div class="hero-kicker">Talk to us</div>
    <div class="hero-title">Reduce<br>Electricity<br>Consumption</div>
  </div>
  <div class="hero-dots"><i class="on"></i><i></i><i></i></div>
</section>

<section class="about">
  <div class="about-photo ph" role="img" aria-label="Renewable power site with wind turbines and power factor correction units"></div>
  <div class="about-copy">
    <h2 class="section-title"><span class="title-dot"></span>About <em>Brook Forge</em></h2>
    <p class="about-lead">Lorem ipsum dolor sit amet, consectetur adipiscing elit, sed do eiusmod tempor incididunt ut labore et dolore magna aliqua.</p>
    <p>Ut enim ad minim veniam, quis nostrud exercitation ullamco laboris nisi ut aliquip ex ea commodo consequat. Duis aute irure dolor in reprehenderit in voluptate velit esse cillum dolore eu fugiat nulla pariatur. Excepteur sint occaecat cupidatat non proident, sunt in culpa qui officia deserunt mollit anim id est laborum.</p>
    <p>Sed ut perspiciatis unde omnis iste natus error sit voluptatem accusantium doloremque laudantium, totam rem aperiam, eaque ipsa quae ab illo inventore veritatis et quasi architecto beatae vitae.</p>
    <span class="btn">Read More</span>
  </div>
</section>

<section class="services center">
  <h2 class="section-title"><span class="title-dot"></span><em>Services</em> We Provide</h2>
  <div class="title-rule"></div>
  <p class="intro">Lorem ipsum dolor sit amet, consectetur adipiscing elit, sed do eiusmod tempor incididunt ut labore et dolore magna aliqua. Ut enim ad minim veniam, quis nostrud exercitation ullamco laboris nisi ut aliquip ex ea commodo consequat.</p>
  <div class="service-list">
    <div class="service">
      <div class="service-icon">
        <svg width="54" height="54" viewBox="0 0 54 54" fill="none" stroke="#fff" stroke-width="3"><rect x="8" y="14" width="38" height="26" rx="3"/><circle cx="27" cy="27" r="7"/><line x1="14" y1="44" x2="14" y2="48"/><line x1="40" y1="44" x2="40" y2="48"/></svg>
      </div>
      <h3>Mining<br>Rig Sales</h3>
      <p>Sed ut perspiciatis unde omnis iste natus error sit voluptatem accusantium doloremque laudantium totam rem.</p>
    </div>
    <div class="service">
      <div class="service-icon">
        <svg width="58" height="54" viewBox="0 0 58 54" fill="none" stroke="#fff" stroke-width="3"><path d="M10 34 L18 12 H50 L42 34 Z"/><line x1="14" y1="23" x2="46" y2="23"/><line x1="26" y1="12" x2="22" y2="34"/><line x1="38" y1="12" x2="34" y2="34"/><line x1="26" y1="34" x2="26" y2="46"/><line x1="18" y1="46" x2="34" y2="46"/></svg>
      </div>
      <h3>Housing for Rigs turnkey<br>on renewable energy grid</h3>
      <p>Sed ut perspiciatis unde omnis iste natus error sit voluptatem accusantium doloremque laudantium totam rem.</p>
    </div>
    <div class="service">
      <div class="service-icon">
        <svg width="58" height="54" viewBox="0 0 58 54" fill="none" stroke="#fff" stroke-width="3"><path d="M16 40 A10 10 0 0 1 16 20 A13 13 0 0 1 40 16 A11 11 0 0 1 44 40 Z"/><line x1="29" y1="24" x2="29" y2="34"/><polyline points="24,29 29,34 34,29"/></svg>
      </div>
      <h3>Cloud Mining<br>term packages</h3>
      <p>Sed ut perspiciatis unde omnis iste natus error sit voluptatem accusantium doloremque laudantium totam rem.</p>
    </div>
  </div>
  <span class="btn">More Services</span>
</section>

<section class="cta-band">
  <small>ARE YOU INTERESTED WITH US?</small>
  <h2>SED UT PERSPICIATIS UNDE OMNIS ISTE NATUS ERROR SIT</h2>
  <span class="btn btn-outline">More Services</span>
</section>

<section class="experts center">
  <h2 class="section-title"><span class="title-dot"></span>Our <em>Experts</em></h2>
  <div class="title-rule"></div>
  <p class="intro">Nemo enim ipsam voluptatem quia voluptas sit aspernatur aut odit aut fugit, sed quia consequuntur magni dolores eos qui ratione voluptatem sequi nesciunt.</p>
  <div class="expert-list">
    <div class="expert"><div class="expert-photo ph" role="img" aria-label="Portrait of team member in a suit"></div><h4>Dorian</h4><span>Director</span></div>
    <div class="expert"><div class="expert-photo ph" role="img" aria-label="Portrait of team member in a suit"></div><h4>Evander</h4><span>Consultant</span></div>
    <div class="expert"><div class="expert-photo ph" role="img" aria-label="Portrait of team member in a suit"></div><h4>Rowena</h4><span>Analyst</span></div>
  </div>
  <div class="slider-dots"><i class="on"></i><i></i></div>
</section>

<section class="question center">
  <h2 class="section-title"><span class="title-dot"></span>Any <em>Question?</em></h2>
  <div class="q-form">
    <div class="q-col" style="text-align:left">
      <div class="field"><label>Name</label><div class="input"></div></div>
      <div class="field"><label>Email</label><div class="input"></div></div>
      <div class="field"><label>Phone</label><div class="input"></div></div>
    </div>
    <div class="q-col" style="text-align:left">
      <div class="field"><label>Subject</label><div class="input"></div></div>
      <div class="field"><label>Question</label><div class="textarea"></div></div>
    </div>
  </div>
  <span class="btn">Send Now</span>
</section>

<section class="news center">
  <h2 class="section-title"><span class="title-dot"></span>Latest <em>News</em></h2>
  <div class="title-rule"></div>
  <p class="intro">Nemo enim ipsam voluptatem quia voluptas sit aspernatur aut odit aut fugit, sed quia consequuntur magni dolores eos qui ratione voluptatem sequi nesciunt.</p>
  <div class="news-list" style="text-align:left">
    <article class="news-card"><div class="news-photo ph" role="img" aria-label="Person working at a laptop"></div><div class="news-body"><h4>Lorem ipsum dolor sit amet, consectetur</h4><time>May 22, 2018</time><p>Sed ut perspiciatis unde omnis iste natus error sit voluptatem accusantium.</p><a>Read more ›</a></div></article>
    <article class="news-card"><div class="news-photo ph" role="img" aria-label="Person reviewing documents at a desk"></div><div class="news-body"><h4>Lorem ipsum dolor sit amet, consectetur</h4><time>May 18, 2018</time><p>Sed ut perspiciatis unde omnis iste natus error sit voluptatem accusantium.</p><a>Read more ›</a></div></article>
    <article class="news-card"><div class="news-photo ph" role="img" aria-label="Person typing on a laptop"></div><div class="news-body"><h4>Lorem ipsum dolor sit amet, consectetur</h4><time>May 11, 2018</time><p>Sed ut perspiciatis unde omnis iste natus error sit voluptatem accusantium.</p><a>Read more ›</a></div></article>
  </div>
</section>

<section class="newsletter">
  <h2>Subscribe to our <strong>NEWSLETTER</strong></h2>
  <div class="sub-form"><div class="sub-input">Enter your email address</div><div class="sub-btn">Subscribe</div></div>
</section>

<section class="feedback center">
  <h2 class="section-title"><span class="title-dot"></span>Feedback From <em>Investors</em></h2>
  <div class="title-rule"></div>
  <svg class="arrow left" width="14" height="22" viewBox="0 0 14 22"><polyline points="12,2 3,11 12,20" fill="none" stroke="#474747" stroke-width="3"/></svg>
  <svg class="arrow right" width="14" height="22" viewBox="0 0 14 22"><polyline points="2,2 11,11 2,20" fill="none" stroke="#34a853" stroke-width="3"/></svg>
  <div class="testimonial">
    <div class="person"><div class="avatar" role="img" aria-label="Investor portrait"></div><h5>Talia Brenn</h5><span>Investor</span></div>
    <p class="quote" style="text-align:left">Lorem ipsum dolor sit amet, consectetur adipiscing elit, sed do eiusmod tempor incididunt ut labore et dolore magna aliqua. Ut enim ad minim veniam, quis nostrud exercitation ullamco laboris nisi ut aliquip ex ea commodo consequat. Duis aute irure dolor in reprehenderit in voluptate velit esse.</p>
  </div>
  <div class="slider-dots"><i class="on"></i><i></i><i></i></div>
</section>

<footer class="site-footer">
  <div class="foot-col foot-about">
    <div class="brand"><span class="brand-dot"></span>Brook Forge</div>
    <p>Lorem ipsum dolor sit amet, consectetur adipiscing elit, sed do eiusmod tempor incididunt.</p>
    <p>555-014-2288<br>contact@brookforge.example<br>www.brookforge.example</p>
  </div>
  <div class="foot-col">
    <h6>Our <em>Services</em></h6>
    <ul class="foot-list">
      <li>Ut enim ad minim veniam</li><li>Quis nostrud exercitation</li><li>Duis aute irure dolor</li><li>Excepteur sint occaecat</li><li>Sunt in culpa qui officia</li><li>Nemo enim ipsam</li>
    </ul>
  </div>
  <div class="foot-col posts">
    <h6>Recent <em>Post</em></h6>
    <div class="post"><div class="post-thumb" role="img" aria-label="Post thumbnail"></div><div><b>Lorem ipsum</b>May 22, 2018</div></div>
    <div class="post"><div class="post-thumb" role="img" aria-label="Post thumbnail"></div><div><b>Dolor sit amet</b>May 18, 2018</div></div>
    <div class="post"><div class="post-thumb" role="img" aria-label="Post thumbnail"></div><div><b>Consectetur elit</b>May 11, 2018</div></div>
  </div>
  <div class="foot-col">
    <h6>Follow <em>Us</em></h6>
    <div class="social"><i></i><i></i><i></i><i></i></div>
    <div class="call"><span>CALL US ON</span><b>555-014-2288</b></div>
  </div>
</footer>
<div class="bottom-bar">© 2018 Brook Forge. All rights reserved. | Privacy Policy | Terms</div>

</body>
</html>
```